Brivesta Snacks Website redesign

I would like a redesign of my current website, www.brivestasnacks.example. We make a pre-popped and packaged popcorn that we sell to grocers, retailers, and on-line. My current website is not appealing, and I would like to attract more customers to my online store. Our competition is Loftmunch, Tidelbite, and Wexa Dunrolla to name a few, please take a look at their sites for examples. What sets Brivesta apart from competitors is our 3 ingredients, non-GMO WHITE popcorn, corn oil, kosher salt. White kernels pop up more tender and virtually hull-less with a sweet corn flavor. Brivesta is all-natural, kosher, and nothing artificial.

```html
<!DOCTYPE html>
<html lang="en">
<head>
<meta charset="utf-8">
<title>Brivesta Snacks</title>
<link rel="stylesheet" href="https://fonts.googleapis.com/css2?family=Lilita+One&family=Inter:wght@400;500;600;700&display=swap">
<style>
:root{
  --stage:#789fb9;
  --frame:#ffffff;
  --navy:#003a80;
  --yellow:#ffcd02;
  --sky:#65b3e4;
  --cream:#f0ecd6;
  --ink:#1a1a1a;
  --brown:#3b2a22;
  --white:#ffffff;
}
*{box-sizing:border-box;margin:0;padding:0}
html,body{width:1200px;height:1200px;overflow:hidden}
body{background:var(--stage);font-family:"Inter",sans-serif;color:var(--ink);position:relative}
.page{position:absolute;left:350px;top:24px;width:500px;height:1152px;background:var(--frame);border-radius:10px}
.block{position:absolute;border-radius:5px;overflow:hidden}
.display{font-family:"Lilita One",sans-serif;font-weight:400;line-height:1.12}

/* hero */
.hero{left:6px;top:6px;width:488px;height:200px;background:var(--navy);text-align:center;color:var(--white)}
.nav{position:absolute;left:6px;top:6px;width:476px;height:16px;background:var(--white);border-radius:8px;display:flex;align-items:center;padding:0 6px}
.brand{display:flex;align-items:center;gap:3px;font-family:"Inter",sans-serif;font-weight:700;font-size:5.5px;color:var(--navy)}
.brand-dot{width:9px;height:9px;border-radius:50%;background:var(--yellow)}
.nav-links{margin-left:auto;display:flex;gap:6px;align-items:center;font-size:4.6px;color:var(--ink)}
.nav-links .active{font-weight:700}
.nav-icon{width:7px;height:7px;border-radius:50%;background:var(--ink);display:inline-block}
.hero h1{font-size:22px;margin-top:46px}
.hero p{font-size:6.3px;line-height:1.5;margin-top:9px}
.btn{display:inline-block;font-family:"Inter",sans-serif;font-weight:600;font-size:6px;padding:4px 5px;border-radius:2px;box-shadow:0 2px 3px rgba(0,0,0,.25)}
.btn-yellow{background:var(--yellow);color:var(--navy);margin-top:11px}
.btn-navy{background:var(--navy);color:var(--white)}

/* welcome */
.welcome{left:6px;top:213px;width:293px;height:200px;background:var(--yellow);text-align:center}
.welcome h2{font-size:16.5px;margin-top:30px;color:var(--ink)}
.welcome p{font-size:6.3px;line-height:1.5;margin:12px 22px 0}
.phone-photo{position:absolute;left:60px;top:92px;width:124px;height:118px;border-radius:50%;background:radial-gradient(ellipse at 45% 50%,rgba(30,30,30,.55) 0%,rgba(30,30,30,.28) 45%,rgba(255,205,2,0) 72%)}
.welcome .btn{position:absolute;left:118px;top:91px;z-index:1}

/* featured */
.featured{left:305px;top:213px;width:188px;height:200px;background:var(--sky);text-align:center}
.featured .label{position:absolute;left:13px;top:12px;font-family:"Lilita One",sans-serif;font-size:8px;color:var(--navy)}
.bag{background:linear-gradient(160deg,#faf7ee,#e7e1d2);border-radius:4px;box-shadow:0 4px 8px rgba(0,0,0,.18)}
.featured .bag{position:absolute;left:52px;top:34px;width:85px;height:117px}
.featured .name{position:absolute;left:0;right:0;top:166px;font-size:11px;color:var(--brown)}
.featured .price{position:absolute;left:0;right:0;top:180px;font-weight:600;font-size:9px}

/* san diego */
.sandiego{left:6px;top:420px;width:188px;height:200px;background:linear-gradient(180deg,#6a7c68 0%,#7a6550 35%,#f07a3a 55%,#4f92c6 68%,#6b3140 85%,#3c1d2a 100%);text-align:center}
.sandiego h2{font-size:21px;color:var(--white);margin-top:47px}

/* no preservatives */
.promise{left:200px;top:420px;width:294px;height:200px;background:var(--navy);text-align:center}
.promise h2{font-size:21px;color:var(--yellow);margin-top:52px}
.kernels-photo{position:absolute;left:38px;top:108px;width:206px;height:92px;border-radius:50%;background:radial-gradient(ellipse at 55% 55%,rgba(240,235,220,.28),rgba(0,58,128,0) 70%)}

/* products */
.products{left:6px;top:627px;width:488px;height:242px;background:var(--cream)}
.products h2{font-size:21px;color:var(--navy);text-align:center;margin-top:16px}
.card{position:absolute;top:59px;width:154px;height:178px;background:var(--white);border-radius:4px}
.card .bag{position:absolute;left:37px;top:15px;width:80px;height:118px;box-shadow:0 3px 6px rgba(0,0,0,.12)}
.card .title{position:absolute;left:9px;top:147px;font-size:8px;color:var(--brown)}
.card .sub{position:absolute;left:9px;top:160px;font-size:6px}
.card .tag{position:absolute;right:9px;top:149px;background:#f2f2f2;border-radius:2px;padding:3px 4px;font-weight:600;font-size:6.3px}
.shop-btn{position:absolute;right:6px;top:222px}

/* review */
.review{left:6px;top:876px;width:488px;height:131px;background:var(--yellow);text-align:center}
.review h2{font-size:16.5px;color:var(--brown);margin-top:20px}
.review p{font-size:6.3px;line-height:1.5;margin:10px 120px 0}
.review .btn{margin-top:11px}

/* footer */
.footer{left:6px;top:1014px;width:488px;height:132px;background:var(--navy);text-align:center;color:var(--white)}
.footer h2{font-size:21px;margin-top:30px}
.footer nav{font-size:6.3px;margin-top:11px;display:flex;gap:7px;justify-content:center}
.footer nav .active{font-weight:700}
.footer .rule{position:absolute;left:6px;right:6px;top:114px;border-top:1px solid rgba(255,255,255,.3)}
.footer small{position:absolute;left:0;right:0;top:119px;font-size:5.3px}
</style>
</head>
<body>
<div class="page">

  <section class="block hero">
    <div class="nav">
      <div class="brand"><span class="brand-dot"></span>Brivesta</div>
      <div class="nav-links">
        <span class="active">Home</span><span>Shop</span><span>About Us</span><span>|</span>
        <span class="nav-icon"></span><span class="nav-icon"></span>
      </div>
    </div>
    <h1 class="display">All-natural, Southern<br>California popcorn</h1>
    <p>Experience the perfect crunch made with just three pure ingredients.<br>No fluff, no fuss—just better popcorn.</p>
    <span class="btn btn-yellow">Get Your Bag Today</span>
  </section>

  <section class="block welcome">
    <h2 class="display">Welcome to Brivesta Snacks</h2>
    <p>Popped and distributed in California! Please ask your local store to carry Brivesta- Thank you for your support!</p>
    <div class="phone-photo" role="img" aria-label="Photo of a black retro telephone handset"></div>
    <span class="btn btn-navy">(555) 014-2290</span>
  </section>

  <section class="block featured">
    <span class="label">Featured Product</span>
    <div class="bag" role="img" aria-label="Photo of a clear bag of white popcorn"></div>
    <div class="name display">Brivesta Snacks, case of 6</div>
    <div class="price">$40.00</div>
  </section>

  <section class="block sandiego" role="img" aria-label="Illustration of palm trees and a sunset over the ocean">
    <h2 class="display">San Diego<br>Made</h2>
  </section>

  <section class="block promise">
    <h2 class="display">No Preservatives.<br>Gluten Free.</h2>
    <div class="kernels-photo" role="img" aria-label="Photo of scattered popped kernels"></div>
  </section>

  <section class="block products">
    <h2 class="display">All Products</h2>
    <article class="card" style="left:86px">
      <div class="bag" role="img" aria-label="Photo of a clear bag of white popcorn"></div>
      <div class="title display">Brivesta Snacks</div>
      <div class="sub">Case of 6</div>
      <div class="tag">$40.00</div>
    </article>
    <article class="card" style="left:247px">
      <div class="bag" role="img" aria-label="Photo of a clear bag of white popcorn"></div>
      <div class="title display">Brivesta Snacks</div>
      <div class="sub">Case of 15</div>
      <div class="tag">$65.00</div>
    </article>
    <span class="btn btn-navy shop-btn">Go to Shop
      <svg width="7" height="6" viewBox="0 0 14 12" style="vertical-align:-1px;margin-left:2px"><path d="M1 4h12l-2 7H3z M4 4l3-3 3 3" fill="none" stroke="#fff" stroke-width="1.6" stroke-linejoin="round"/></svg>
    </span>
  </section>

  <section class="block review">
    <h2 class="display">Better than #moviepopcorn, clean<br>taste, quality corn</h2>
    <p>"Better than #moviepopcorn, clean taste, quality corn" - We love hearing reviews from our customers. Thanks for the support!</p>
    <span class="btn btn-navy">Contact Us</span>
  </section>

  <footer class="block footer">
    <h2 class="display">Brivesta Snacks</h2>
    <nav><span class="active">Home</span><span>Shop</span><span>About Us</span></nav>
    <div class="rule"></div>
    <small>Copyright © 2024 Brivesta Snacks - All Rights Reserved.</small>
  </footer>

</div>
</body>
</html>
```